Business Card Design

Bramwell Pantry is the name of my health coaching business. My tag line is "Where good health meets real life." I will be working with clients one-on-one and in groups. My target clients are women "of a certain age" who want to be more comfortable in their own skin. We will work together in a 6-month program. The coaching sessions will take place in my kitchen. I will also be conducting monthly cooking classes and field trips - to farmer's markets, speciality markets etc.. for my clients.
Updates

the business name is Bramwell Pantry - I'm not sure how the p got in there at the end of the name

Thank you

Please include the website - www.bramwellpantry-example.com and the tag line:

Where good health meets real life on the business card.

Thank you

Please add the phone number to the business card - sorry, I forgot to state that in the original brief

(555) 218-4476

Target Market(s)

Women "of a certain age" who want to be more comfortable in their own skin

Industry/Entity Type

Cooking

Contact Information for Business Card

Bramwell Pantry
Where good health meets real life

Harriet Dunmore
Health Coach
(555) 218-4476

Font styles to use
Serif
Sans Serif

Requirements
Must have
• front & back design
I typical like soft colors - and have tended toward greens over time - I'm open although I would not like bright reds, yellows etc..

```html
<!DOCTYPE html>
<html lang="en">
<head>
<meta charset="utf-8">
<title>Bramwell Pantry — Business Card</title>
<link href="https://fonts.googleapis.com/css2?family=Righteous&family=Great+Vibes&family=Questrial&display=swap" rel="stylesheet">
<style>
  :root {
    --page-bg: #e9e6df;
    --green-deep: #1d4710;
    --green-mid: #3f7a22;
    --green-glow: #9cc940;
    --lime: #b9dc4c;
    --white: #ffffff;
    --ink-light: #f3f7ea;
  }
  html, body {
    margin: 0;
    width: 1200px;
    height: 900px;
    overflow: hidden;
    background: var(--page-bg);
  }
  .canvas {
    position: relative;
    width: 1200px;
    height: 900px;
  }
  .card {
    position: absolute;
    left: 260px;
    width: 680px;
    height: 389px;
    border-radius: 26px;
    overflow: hidden;
    box-shadow: 0 10px 26px rgba(0,0,0,0.22);
    background:
      repeating-linear-gradient(90deg, rgba(255,255,255,0.035) 0 2px, rgba(0,0,0,0.03) 2px 5px),
      radial-gradient(ellipse 70% 80% at 50% 20%, var(--green-glow) 0%, var(--green-mid) 45%, var(--green-deep) 100%);
  }
  .card--front { top: 40px; }
  .card--back { top: 471px; }

  .brand {
    display: flex;
    align-items: center;
    gap: 16px;
    font-family: "Righteous", sans-serif;
    color: var(--white);
    letter-spacing: 1px;
  }
  .brand__mark {
    background: var(--green-deep);
    flex: none;
  }
  .card--front .brand {
    position: absolute;
    left: 0; right: 0;
    top: 120px;
    justify-content: center;
    font-size: 58px;
  }
  .card--front .brand__mark { width: 54px; height: 54px; }
  .tagline {
    position: absolute;
    left: 0; right: 0;
    top: 228px;
    text-align: center;
    font-family: "Great Vibes", cursive;
    font-size: 44px;
    color: var(--white);
  }

  .card--back .brand {
    position: absolute;
    left: 40px;
    top: 40px;
    font-size: 28px;
    gap: 12px;
  }
  .card--back .brand__mark { width: 30px; height: 30px; }
  .holder {
    position: absolute;
    left: 210px;
    top: 130px;
    font-family: "Righteous", sans-serif;
  }
  .holder__name {
    font-size: 40px;
    color: var(--lime);
    margin: 0;
  }
  .holder__role {
    font-size: 19px;
    color: var(--lime);
    margin: 2px 0 0 150px;
  }
  .contact {
    position: absolute;
    right: 40px;
    bottom: 46px;
    margin: 0;
    padding: 0;
    list-style: none;
    font-family: "Questrial", sans-serif;
    font-size: 21px;
    color: var(--ink-light);
    text-align: right;
  }
  .contact__item {
    display: flex;
    justify-content: flex-end;
    align-items: center;
    gap: 12px;
    margin-top: 8px;
  }
  .contact__icon { width: 24px; height: 24px; flex: none; }
</style>
</head>
<body>
<main class="canvas">
  <section class="card card--front" aria-label="Card front">
    <div class="brand"><span class="brand__mark"></span><span class="brand__name">Bramwell Pantry</span></div>
    <p class="tagline">“Where good health meets real life”</p>
  </section>

  <section class="card card--back" aria-label="Card back">
    <div class="brand"><span class="brand__mark"></span><span class="brand__name">Bramwell Pantry</span></div>
    <div class="holder">
      <p class="holder__name">Harriet Dunmore</p>
      <p class="holder__role">Health Coach</p>
    </div>
    <ul class="contact">
      <li class="contact__item">(555) 218-4476
        <svg class="contact__icon" viewBox="0 0 24 24"><circle cx="12" cy="12" r="12" fill="#b9dc4c"/><path d="M8 6.5l2 0 1 3-1.5 1a7 7 0 0 0 4 4l1-1.5 3 1v2c0 .8-.7 1.5-1.5 1.5A10 10 0 0 1 6.5 8c0-.8.7-1.5 1.5-1.5z" fill="#1d4710"/></svg>
      </li>
      <li class="contact__item">harriet@bramwellpantry-example.com
        <svg class="contact__icon" viewBox="0 0 24 24"><circle cx="12" cy="12" r="12" fill="#b9dc4c"/><rect x="6" y="8" width="12" height="8.5" rx="1" fill="#1d4710"/><path d="M6.5 8.7l5.5 4 5.5-4" stroke="#b9dc4c" stroke-width="1.2" fill="none"/></svg>
      </li>
      <li class="contact__item">www.bramwellpantry-example.com
        <svg class="contact__icon" viewBox="0 0 24 24"><circle cx="12" cy="12" r="12" fill="#b9dc4c"/><circle cx="12" cy="12" r="6" fill="none" stroke="#1d4710" stroke-width="1.4"/><ellipse cx="12" cy="12" rx="2.6" ry="6" fill="none" stroke="#1d4710" stroke-width="1.2"/><path d="M6 12h12" stroke="#1d4710" stroke-width="1.2"/></svg>
      </li>
    </ul>
  </section>
</main>
</body>
</html>
```